Kestrel Works Business Cards

This job is for the design of a business card.
I would like to review the design in 2x colour tones to choose from black and white inverted.
EG:
Black with white logo and white with black logo on BACK
White with black text on front and black with white text options
PRINTING DIMENSIONS: 4.5 x 8.5cm
Complete design will need to be provided in ready to print format with bleed lines
Target Market(s)
The audience of my business are people in the trade industry.
It will be also used for general networking with trades people and possible future clients.
I want to be represented as a professional, dynamic, creative and personable operator.
The card should reflect style, taste, experience, professionalism.
Industry/Entity Type
Business
Requirements
Must have
- BACK CONTENT:
- Logo in white and black background and vice versa with WHITE card and black logo review samples.
- FRONT CARD CONTENT:
- Name: Morgan Telvane
- Director
- Phone: 0438 216 947
- Email: morgan@kestrelworks.com.au
- Web: kestrelworks.com.au
- LICENCE #: KT-R 72158
Nice to have
- Possibly a textured background design on rear as a pose to a solid black
- Possibly adding a blue or orange discreet colour tone (possibly for email, phone abbreviated letter or symbols).

```html
<!DOCTYPE html>
<html lang="en">
<head>
<meta charset="utf-8">
<title>Kestrel Works Business Cards</title>
<link rel="stylesheet" href="https://fonts.googleapis.com/css2?family=Questrial&display=swap">
<style>
  :root {
    --stage: #2a2a2a;
    --card-white: #f7f7f7;
    --card-black: #0d0d0d;
    --ink-dark: #111111;
    --ink-light: #f2f2f2;
    --accent-blue: #3fa9e0;
    --pattern-light-a: #f1f1f1;
    --pattern-light-b: #e6e6e6;
    --pattern-dark-a: #141414;
    --pattern-dark-b: #1c1c1c;
  }
  * { box-sizing: border-box; margin: 0; padding: 0; }
  html, body {
    width: 1200px;
    height: 900px;
    overflow: hidden;
    background: var(--stage);
    font-family: "Questrial", "Helvetica Neue", Arial, sans-serif;
  }
  .card {
    position: absolute;
    width: 510px;
    height: 270px;
    overflow: hidden;
    box-shadow: 0 10px 30px rgba(0,0,0,0.5);
  }
  .card--back { left: 220px; top: 120px; background: var(--card-white); }
  .card--front { left: 470px; top: 490px; background: var(--card-black); }

  .card__pattern { position: absolute; inset: 0; }
  .card--back .card__pattern {
    background: linear-gradient(135deg, var(--pattern-light-a), var(--pattern-light-b));
  }
  .card--front .card__pattern {
    background: linear-gradient(135deg, var(--pattern-dark-b), var(--pattern-dark-a));
  }

  .brand {
    position: absolute;
    display: flex;
    flex-direction: column;
    align-items: flex-end;
  }
  .brand__name {
    display: flex;
    align-items: center;
    gap: 10px;
    letter-spacing: 1px;
    line-height: 1;
    white-space: nowrap;
  }
  .brand__mark {
    display: inline-block;
    border: 2px solid currentColor;
  }
  .brand__tagline { letter-spacing: 5px; margin-top: 6px; }

  .card--back .brand {
    left: 0; right: 0; top: 100px;
    align-items: center;
    color: var(--ink-dark);
  }
  .card--back .brand__name { font-size: 46px; }
  .card--back .brand__mark { width: 26px; height: 26px; }
  .card--back .brand__tagline { font-size: 11px; }

  .card--front .brand { right: 26px; top: 28px; color: var(--ink-light); }
  .card--front .brand__name { font-size: 27px; }
  .card--front .brand__mark { width: 16px; height: 16px; }
  .card--front .brand__tagline { font-size: 7px; letter-spacing: 3px; }

  .contact {
    position: absolute;
    right: 26px;
    top: 110px;
    text-align: right;
    color: var(--ink-light);
    font-size: 13px;
    line-height: 1.3;
  }
  .contact__name { color: var(--accent-blue); font-size: 15px; letter-spacing: 1px; }
  .contact__role { margin-bottom: 6px; }
  .contact__row {
    display: flex;
    justify-content: flex-end;
    align-items: center;
    gap: 6px;
    height: 19px;
    white-space: nowrap;
  }
  .contact__icon { width: 14px; height: 14px; flex: none; }
  .contact__line { margin-top: 6px; white-space: nowrap; }
  .contact__web { font-size: 14px; letter-spacing: 0.5px; white-space: nowrap; }
</style>
</head>
<body>

<section class="card card--back" aria-label="Card back">
  <div class="card__pattern" role="img" aria-label="Faint repeating brand-name texture on white"></div>
  <div class="brand">
    <div class="brand__name"><span class="brand__mark"></span>KESTREL WORKS</div>
    <div class="brand__tagline">CONSTRUCTION GROUP</div>
  </div>
</section>

<section class="card card--front" aria-label="Card front">
  <div class="card__pattern" role="img" aria-label="Faint repeating brand-name texture on black"></div>
  <div class="brand">
    <div class="brand__name"><span class="brand__mark"></span>KESTREL WORKS</div>
    <div class="brand__tagline">CONSTRUCTION GROUP</div>
  </div>
  <div class="contact">
    <div class="contact__name">MORGAN TELVANE</div>
    <div class="contact__role">Director</div>
    <div class="contact__row">0438 216 947
      <svg class="contact__icon" viewBox="0 0 14 14" aria-hidden="true">
        <circle cx="7" cy="7" r="6.2" fill="none" stroke="#3fa9e0" stroke-width="1"/>
        <path d="M4.6 4.2c.4-.4.8-.3 1 .1l.5.9c.2.3.1.6-.2.8l-.3.2c.3.7.9 1.3 1.6 1.6l.2-.3c.2-.3.5-.4.8-.2l.9.5c.4.2.5.6.1 1-.6.6-1.4.7-2.2.2-1.1-.6-2-1.5-2.6-2.6-.4-.8-.4-1.6.2-2.2z" fill="#3fa9e0"/>
      </svg>
    </div>
    <div class="contact__row">kestrelworks.com.au
      <svg class="contact__icon" viewBox="0 0 14 14" aria-hidden="true">
        <circle cx="7" cy="7" r="6.2" fill="none" stroke="#3fa9e0" stroke-width="1"/>
        <rect x="4" y="4.8" width="6" height="4.4" fill="none" stroke="#3fa9e0" stroke-width="0.9"/>
        <path d="M4 4.8l3 2.4 3-2.4" fill="none" stroke="#3fa9e0" stroke-width="0.9"/>
      </svg>
    </div>
    <div class="contact__row">LICENCE # KT-R 72158
      <svg class="contact__icon" viewBox="0 0 14 14" aria-hidden="true">
        <circle cx="7" cy="7" r="6.2" fill="none" stroke="#3fa9e0" stroke-width="1"/>
        <path d="M4.5 7.2l1.8 1.8 3.3-3.6" fill="none" stroke="#3fa9e0" stroke-width="1"/>
      </svg>
    </div>
    <div class="contact__line">morgan@kestrelworks.com.au</div>
    <div class="contact__web">www.kestrelworks.com.au</div>
  </div>
</section>

</body>
</html>
```